Business card / stationery design
Pemberton Hale Warrick
Project: Business card / stationery design
Business card / stationery design - Engineering
Creative Brief
Use specific fonts
Gill Sans MT, Calibri, Corbel, Lucida Sans UC or similar
Professional
Derek R. Pemberton, P.E., LEED A.P., CPMP
Principal
4738 E. Harrowgate Ave., Suite C-212B, Springfield, Missouri 65809
dpemberton@pembertonhalewarrick.example
www.pembertonhalewarrick.example
We would like to use only the logo from the attached file. We like the current color arrangement, but would be interested in seeing it in other colors. Also the slightly gray color behind the logo should just be white or whatever the background color is. A couple of examples are attached. The main text adjacent to the logo should read: Pemberton Hale Warrick. Secondary text will be similar to: Engineering & Energy Services.
We are interested in your ideas.

```html
<!DOCTYPE html>
<html lang="en">
<head>
<meta charset="utf-8">
<title>Pemberton Hale Warrick – Business Cards</title>
<link rel="stylesheet" href="https://fonts.googleapis.com/css2?family=Arimo:wght@400;700&family=Lato:wght@400;700&display=swap">
<style>
  :root {
    --page: #ffffff;
    --blue-light: #2a82c4;
    --blue-mid: #1a5f9e;
    --blue-dark: #0b3a72;
    --blue-band: #3d9be0;
    --green-light: #6fb23a;
    --green-mid: #4a8a27;
    --green-dark: #2c5e16;
    --green-band: #8cc656;
    --accent-green: #7dbb3c;
    --gray-light: #ffffff;
    --gray-edge: #c9cdd0;
    --ink: #2f3338;
    --white: #ffffff;
    --tint-blue: #bfe0ff;
    --tint-green: #e4f5cf;
  }
  * { box-sizing: border-box; margin: 0; padding: 0; }
  html, body { width: 1200px; height: 694px; overflow: hidden; background: var(--page); }
  body { position: relative; font-family: "Lato", Arial, sans-serif; }

  .card {
    position: absolute;
    width: 580px; height: 336px;
    border-radius: 14px;
    overflow: hidden;
    color: var(--white);
  }
  .card--front-blue { left: 12px; top: 7px;
    background: linear-gradient(160deg, var(--blue-light) 0%, var(--blue-mid) 45%, var(--blue-dark) 100%); }
  .card--front-green { left: 608px; top: 7px;
    background: linear-gradient(160deg, var(--green-light) 0%, var(--green-mid) 45%, var(--green-dark) 100%); }
  .card--back-light { left: 12px; top: 353px; color: var(--ink);
    background: radial-gradient(ellipse at 45% 40%, var(--gray-light) 0%, #eef0f1 45%, var(--gray-edge) 100%); }
  .card--back-blue { left: 608px; top: 353px;
    background: linear-gradient(180deg, var(--blue-band) 0%, var(--blue-light) 100%); }

  /* brand block on fronts */
  .brand-corner { position: absolute; right: 22px; top: 18px; text-align: right; }
  .brand-corner .brand-square { width: 40px; height: 40px; background: var(--white); margin: 0 14px 6px auto; }
  .brand-name { font-family: "Arimo", Arial, sans-serif; font-weight: 700; text-transform: uppercase; letter-spacing: 0.5px; }
  .brand-corner .brand-name { font-size: 11px; }
  .tagline { font-family: "Lato", Arial, sans-serif; }
  .brand-corner .tagline { font-size: 10px; margin-top: 2px; }

  .person { position: absolute; left: 0; right: 0; top: 136px; text-align: center; }
  .person__name { font-family: "Arimo", Arial, sans-serif; font-weight: 700; font-size: 21px; }
  .person__title { font-size: 15px; margin-top: 3px; }
  .card--front-blue .person__title { color: var(--tint-blue); }
  .card--front-green .person__title { color: var(--tint-green); }

  .address { position: absolute; left: 24px; top: 226px; font-size: 12.5px; line-height: 17px; }
  .contact { position: absolute; left: 292px; top: 226px; font-size: 11.5px; line-height: 17px; }
  .contact__row { display: flex; }
  .contact__label { width: 38px; }
  .contact__value { white-space: nowrap; }

  .web-band {
    position: absolute; left: 0; right: 0; top: 292px; height: 30px;
    display: flex; align-items: center; justify-content: center;
    font-weight: 700; font-size: 15px; letter-spacing: 2px;
  }
  .card--front-blue .web-band { background: var(--blue-band); border-top: 3px solid var(--accent-green); }
  .card--front-green .web-band { background: var(--green-band); border-top: 3px solid var(--green-dark); }

  /* light back */
  .brand-center { position: absolute; left: 0; right: 0; top: 110px; text-align: center; }
  .brand-center .brand-square { width: 66px; height: 66px; background: var(--blue-mid); margin: 0 auto 22px; }
  .card--back-light .brand-name { font-size: 22px; color: var(--ink); }

  /* blue back */
  .band-dark { position: absolute; left: 0; right: 0; top: 84px; height: 198px;
    background: linear-gradient(90deg, var(--blue-mid) 0%, var(--blue-dark) 55%, var(--blue-mid) 100%); }
  .card--back-blue .brand-center { top: 104px; }
  .card--back-blue .brand-square { width: 60px; height: 60px; background: var(--white); margin-bottom: 18px; }
  .card--back-blue .brand-name { font-size: 20px; }
  .card--back-blue .tagline { font-size: 15px; margin-top: 3px; }
</style>
</head>
<body>

<section class="card card--front-blue">
  <div class="brand-corner">
    <div class="brand-square"></div>
    <div class="brand-name">Pemberton Hale Warrick</div>
    <div class="tagline">Engineering &amp; Energy Services</div>
  </div>
  <div class="person">
    <div class="person__name">Derek R. Pemberton, P.E., LEED A.P., CPMP</div>
    <div class="person__title">Principal</div>
  </div>
  <div class="address">4738 E. Harrowgate Ave.,<br>Suite C-212B, Springfield,<br>Missouri 65809</div>
  <div class="contact">
    <div class="contact__row"><span class="contact__label">Phone</span><span class="contact__value">: 417-555-0142</span></div>
    <div class="contact__row"><span class="contact__label">Cell</span><span class="contact__value">: 417-555-0187</span></div>
    <div class="contact__row"><span class="contact__label">Email</span><span class="contact__value">: dpemberton@pembertonhalewarrick.example</span></div>
  </div>
  <div class="web-band">www.pembertonhalewarrick.example</div>
</section>

<section class="card card--front-green">
  <div class="brand-corner">
    <div class="brand-square"></div>
    <div class="brand-name">Pemberton Hale Warrick</div>
    <div class="tagline">Engineering &amp; Energy Services</div>
  </div>
  <div class="person">
    <div class="person__name">Derek R. Pemberton, P.E., LEED A.P., CPMP</div>
    <div class="person__title">Principal</div>
  </div>
  <div class="address">4738 E. Harrowgate Ave.,<br>Suite C-212B, Springfield,<br>Missouri 65809</div>
  <div class="contact">
    <div class="contact__row"><span class="contact__label">Phone</span><span class="contact__value">: 417-555-0142</span></div>
    <div class="contact__row"><span class="contact__label">Cell</span><span class="contact__value">: 417-555-0187</span></div>
    <div class="contact__row"><span class="contact__label">Email</span><span class="contact__value">: dpemberton@pembertonhalewarrick.example</span></div>
  </div>
  <div class="web-band">www.pembertonhalewarrick.example</div>
</section>

<section class="card card--back-light">
  <div class="brand-center">
    <div class="brand-square"></div>
    <div class="brand-name">Pemberton Hale Warrick</div>
  </div>
</section>

<section class="card card--back-blue">
  <div class="band-dark"></div>
  <div class="brand-center">
    <div class="brand-square"></div>
    <div class="brand-name">Pemberton Hale Warrick</div>
    <div class="tagline">Engineering &amp; Energy Services</div>
  </div>
</section>

</body>
</html>
```